Corvel Gulfworks

i need a brochure (more of a company profile for a company that has been in business for a long time). Unfortunately we have never had a proper company profile so basically im looking for a professional brochure that shows the strength of the company and what it does.
CORVEL GULFWORKS is a general contracting & construction company based in Jeddah with operations all over the region. We focus on civil/structural works and have the capabilities of executing electro-mechanical, finishing works and turnkey projects.

Reason: I stil need more designs from other invited designers that have accepted my invitation.

To all designers

I have extended the deadline until December 28th...i hope this will help you with your work

happy holidays to everyone!

Target Market(s)

government, real estate developers, private client/investors

Industry/Entity Type

Construction

Requirements
Must have
• -file named prequalifictaion has all the information necessary to fill up the brochure.
-22-30 pages
-using only the best photos that i have uploaded named project pics.
-A bi-fold brochure measuring 8inches high by 10 inches wide, however i am open for suggestions.
-sorry everyone, i dont have my logo in eps format
Should not have
• too many colors

```html
<!DOCTYPE html>
<html lang="en">
<head>
<meta charset="utf-8">
<title>Corvel Gulfworks – Construction Experience</title>
<link href="https://fonts.googleapis.com/css2?family=Hind:wght@300;400;500&family=Roboto:wght@500;700&display=swap" rel="stylesheet">
<style>
:root{
  --navy:#1b3f6e;
  --grey-dark:#bdbec1;
  --grey-light:#e5e6e7;
  --grey-mid:#c8c9cb;
  --footer:#808184;
  --rule:#8a8b8d;
  --ink:#333;
  --title-grey:#6d6e71;
}
*{margin:0;padding:0;box-sizing:border-box}
html,body{width:1200px;height:900px;overflow:hidden;background:#fff}
body{position:relative;font-family:'Hind',sans-serif;color:var(--ink)}
.spread{position:absolute;left:40px;top:0;width:1123px;height:900px;border-left:1px solid #ddd;border-right:1px solid #ddd}
.spine{position:absolute;left:601px;top:108px;width:1px;height:737px;background:#ddd}
.header-band{position:absolute;left:40px;top:0;width:1123px;height:108px;
  background:linear-gradient(180deg,#c9cacc 0%,#dcdddf 70%,#f4f4f5 100%)}
.footer{position:absolute;left:40px;top:845px;width:1123px;height:55px;background:var(--footer)}
.folio{position:absolute;top:853px;width:200px;text-align:center;color:#fff;font-family:'Roboto',sans-serif;font-weight:500;line-height:1.1}
.folio .name{font-size:11px}
.folio .num{font-size:14px;font-weight:700;letter-spacing:1px}
.folio.left{left:220px}
.folio.right{left:783px}
.tab{position:absolute;top:700px;width:16px;height:90px;background:var(--navy)}
.tab.left{left:40px;border-radius:0 8px 8px 0}
.tab.right{left:1147px;border-radius:8px 0 0 8px}

.title-main{position:absolute;left:145px;top:125px;width:350px;height:36px;border-top:1px solid var(--rule);border-bottom:1px solid var(--rule);
  text-align:center;font-family:'Roboto',sans-serif;font-weight:700;font-size:21px;line-height:36px;color:var(--navy);letter-spacing:.3px}
.title-sub{position:absolute;left:680px;top:132px;width:404px;text-align:center;font-family:'Roboto',sans-serif;font-weight:700;font-size:14px;color:var(--title-grey)}
.intro{position:absolute;left:97px;top:211px;width:450px;font-size:10.5px;line-height:13px}

.table{position:absolute;width:447px;font-size:12px;line-height:15px}
.table.left{left:97px;top:254px}
.table.right{left:659px;top:256px}
.thead{display:grid;grid-template-columns:61px 82px 1fr;height:22px;margin-bottom:4px;border-bottom:1px dotted var(--rule)}
.thead span{background:var(--navy);color:#fff;padding:3px 0 0 6px;font-size:11.5px;border-left:1px solid #fff}
.thead span:first-child{border-left:none}
.entry{display:grid;grid-template-columns:61px 82px 1fr;border-bottom:1px dotted var(--rule)}
.entry.dark{background:var(--grey-dark)}
.entry.light{background:var(--grey-light)}
.year{padding:3px 0 0 2px}
.price{padding:3px 8px 0 0;text-align:right}
.desc .line{padding:3px 4px 2px 2px;border-bottom:1px dotted var(--rule)}
.desc .line:last-child{border-bottom:none}
.scope{list-style:none;padding:3px 4px 4px 2px}
.scope li{padding-left:18px;text-indent:-18px;margin-bottom:4px}
.scope li.gap{margin-bottom:9px}
sup{font-size:7px;line-height:0}

.gallery{position:absolute;left:602px;top:619px;width:504px;height:202px;background:var(--grey-mid)}
.photo{position:absolute}
.photo.towers{left:659px;top:624px;width:303px;height:193px;background:linear-gradient(180deg,#a9cbe6 0%,#e8eef2 45%,#b9b7a9 75%,#8f8c84 100%)}
.photo.site{left:966px;top:624px;width:136px;height:193px;background:linear-gradient(180deg,#9fc0dc 0%,#c48a5a 40%,#a5653f 75%,#7d6a5a 100%)}
</style>
</head>
<body>
<div class="header-band" role="img" aria-label="Decorative dotted band with city skyline silhouette"></div>
<div class="spread"></div>
<div class="spine"></div>

<section class="page page-left">
  <h1 class="title-main">CONSTRUCTION EXPERIENCE</h1>
  <p class="intro">CORVEL GULFWORKS CO. LTD., has many projects and has demonstrated its versatility by supplying products of the highest quality for use in a broad range of structures.</p>

  <div class="table left">
    <div class="thead"><span>Year</span><span>Contract Price</span><span>Description</span></div>

    <div class="entry dark">
      <div class="year">1993</div><div class="price">1,600,000</div>
      <div class="desc">
        <div class="line">Regional Conference Center (RCC) in Riyadh.</div>
        <div class="line">Concrete &amp; Finishing Works.</div>
        <div class="line">Main Entrance Gate – Driver’s Saloon (2 Nos) - Helipad. - Gas Tank.</div>
      </div>
    </div>
    <div class="entry light">
      <div class="year">1993</div><div class="price">13,000,000</div>
      <div class="desc">
        <div class="line">Al Noor Residence Palace in Jeddah (Obhur).</div>
        <div class="line">Concrete &amp; Finishing Works.</div>
        <div class="line">Sons Villa (3 Nos) – Guest Villa (3 Nos) - Men Quarter (1 No) - Electrical Sub-station (3 Nos) – External &amp; Internal Boundary Wall - Guard Houses (9 Nos) - Family Entrance (1 No) - Septic Tank (2 Nos).</div>
      </div>
    </div>
    <div class="entry dark">
      <div class="year">1993</div><div class="price">8,000,000</div>
      <div class="desc">
        <div class="line">Marina Plaza (Commercial Center) in Jeddah.</div>
        <div class="line">Concrete Works – Steel Works.</div>
        <div class="line">7 Storey Building ( 7000 m<sup>2</sup>/Storey).</div>
      </div>
    </div>
    <div class="entry light">
      <div class="year">1993</div><div class="price">6,000,000</div>
      <div class="desc">
        <div class="line">Al Waha Palace in Madina Quba.</div>
        <div class="line">Concrete &amp; Finishing Works.</div>
        <div class="line">Officer’s Building - Al-Rawdah Buildings (3 Nos) - Diwanieh &amp; Waiting - Family entrance gate – Under ground water tank - Electrical Sub-station.</div>
      </div>
    </div>
    <div class="entry dark">
      <div class="year">1994</div><div class="price">1,500,000</div>
      <div class="desc">
        <div class="line">WareHouse in Jeddah(Briman).</div>
        <div class="line">Concrete Works – Steel Works.</div>
      </div>
    </div>
    <div class="entry light">
      <div class="year">1995</div><div class="price">1,500,000</div>
      <div class="desc">
        <div class="line">Staff House Building in Jeddah (Obhur).</div>
        <div class="line">Turnkey job.</div>
        <div class="line">200 m<sup>2</sup> on Turnkey basis (Construction, Finishing and Furniture.</div>
      </div>
    </div>
  </div>
</section>

<section class="page page-right">
  <h2 class="title-sub">CONSTRUCTION EXPERIENCE</h2>
  <div class="table right">
    <div class="thead"><span>Year</span><span>Contract Price</span><span>Description</span></div>
    <div class="entry dark">
      <div class="year">1995 - 96</div><div class="price">32,500,000</div>
      <div class="desc">
        <div class="line">Al Sahil Towers in Jeddah (Corniche).</div>
        <ul class="scope">
          <li style="text-indent:0;padding-left:0">Concrete Works – Steel Works.</li>
          <li>(a) 4 Towers of 13 floors (each). Each floor is two flats of 900 m<sup>2</sup>. Total built areas of Towers 46,800 m<sup>2</sup>.</li>
          <li>(b) Villa on Top - Duplex villas with swimming pool over each Tower.</li>
          <li>(c) Water Tank # 1 - At the North West part of the project (2700 m3).</li>
          <li>(d) Water Tank # 2 - At the North East part of the project (1,200 m<sup>3</sup>).</li>
          <li class="gap">(e) Holding Tank # 1 - At the West Side of the project (1,000 m<sup>3</sup>).</li>
          <li>(f) Holding Tank # 2 - At the East Side of the project (800 m<sup>3</sup>).</li>
          <li class="gap">(g) North Basement - For parking and drivers rooms (4,500 m<sup>2</sup>).</li>
          <li>(h) Swimming Pools - Area of 900 m<sup>2</sup>.</li>
        </ul>
      </div>
    </div>
  </div>

  <div class="gallery"></div>
  <div class="photo towers" role="img" aria-label="Photo of completed white residential towers beside a palm-lined road"></div>
  <div class="photo site" role="img" aria-label="Photo of a high-rise tower under construction with cranes"></div>
</section>

<div class="tab left"></div>
<div class="tab right"></div>
<footer class="footer"></footer>
<div class="folio left"><div class="name">Corvel Gulfworks</div><div class="num">. 10 .</div></div>
<div class="folio right"><div class="name">Corvel Gulfworks</div><div class="num">. 11 .</div></div>
</body>
</html>
```